Email mail merge - not a marketing email, this is an update email sent regularly to our members

HI I need a generic email designed to send out to our members, this is a tri-weekly (monday - updates - Wednesday - updates and Fridays - weekly round up.

we would like it to have within the mail body, 3 interactive, changeable boxes for example "quote of the week', 'top performer' and something else, It would be great if we can remove a box if and when we choose.
Our company is called Kl4vo Amusements or Kl4vo for short.
It needs to be in HTML to fit with our back office software.
We have all the logos for you already which I have included, I have also included our current email header.
our websites are...
kl4vamu.cub - This is our members back end site.
kl4vamu.com - This is our gaming site.
Please email me on derek@kl4vamu.com if you have any queries

Target Market(s)

All of our members - We currently have over 400 but it is growing at an astronomical rate.

Industry/Entity Type

Marketing

Font styles to use
Serif
Decorative
Script

Requirements
Must have
• At least two interactive, changeable boxes/areas that I can put photo's or quotes in to. I would also like some guidelines as to how I change these myself.
• The colours should be inline with our kl4vamu.club site.
Nice to have
• This is a positive email update so it needs to look clean and clear but vibrant, we are a unique company that is breaking records and is very successful.
• Our members have the ability and some already are earning vast sums of money.

```html
<!DOCTYPE html>
<html lang="en">
<head>
<meta charset="utf-8">
<title>Kl4vo Amusements – Member Update</title>
<link rel="stylesheet" href="https://fonts.googleapis.com/css2?family=Lato:ital,wght@0,400;0,700;1,400&family=Roboto+Slab:wght@400&family=Indie+Flower&display=swap">
<style>
:root{
  --teal:#12b09a;
  --teal-dark:#0e9c88;
  --ink:#2b2b2b;
  --grey:#6f7577;
  --page:#f0eff0;
  --card:#ffffff;
  --banner:#232a29;
  --tab:#f1f1f1;
  --line:#d7d7d7;
}
*{box-sizing:border-box;margin:0;padding:0}
html,body{width:1200px;height:2323px;overflow:hidden}
body{background:var(--page);font-family:"Lato",Arial,sans-serif;color:var(--ink);position:relative}
.abs{position:absolute}
.preheader{top:56px;left:0;width:1200px;text-align:center;font-size:17px}
.preheader a{color:var(--teal-dark);font-style:italic;font-weight:700;text-decoration:underline}
.mail{top:124px;left:164px;width:875px;height:2041px;background:var(--card);border-top:5px solid var(--teal);border-bottom:6px solid var(--teal)}
.brand{font-family:"Lato",Arial,sans-serif;font-weight:400;color:var(--grey);white-space:nowrap;display:flex;align-items:center;gap:10px}
.brand-dot{width:14px;height:14px;border-radius:50%;background:var(--teal);flex:none}
.brand-top{top:160px;left:203px;font-size:32px;line-height:44px}
.contact-btn{height:40px;top:169px;background:#eef1f1;border:1px solid #cfd8d6;border-left:5px solid var(--teal);font-family:"Roboto Slab",Georgia,serif;font-size:15px;display:flex;align-items:center;gap:8px;padding-left:16px;color:#333;white-space:nowrap}
.contact-mail{left:585px;width:234px}
.contact-phone{left:825px;width:175px;padding-left:14px}
.hero{top:249px;left:203px;width:799px;height:345px;background:linear-gradient(180deg,#0e1a3a 0%,#27335d 45%,#4b3a6a 70%,#1c1f38 100%)}
.section-title{font-weight:700;color:var(--teal);font-size:17px;left:203px}
.section-rule{left:203px;width:34px;height:2px;background:var(--teal)}
.about{top:670px;left:203px;width:800px;font-size:15.5px;line-height:23px}
.btn{background:var(--teal);color:#fff;font-weight:700;font-size:15px;display:flex;align-items:center;justify-content:center}
.read-more{top:769px;left:203px;width:148px;height:39px;border-left:4px solid var(--teal-dark)}
.offer{top:834px;left:203px;width:799px;height:155px;background:var(--banner)}
.offer-title{top:866px;left:238px;font-size:29px;color:var(--teal);display:flex;align-items:center;gap:10px}
.script{font-family:"Indie Flower",cursive}
.offer-sub{top:908px;left:238px;font-size:17px;color:#d9dedd}
.offer-btn{top:950px;left:238px;width:353px;height:39px}
.agent{top:766px;left:828px;width:186px;height:223px;background:linear-gradient(180deg,#f3ece6 0%,#e8ddd2 55%,#f7f7f7 100%);border-radius:90px 90px 0 0}
.invite{top:1046px;left:203px;width:305px;font-size:15.3px;line-height:22px}
.invite p+p{margin-top:7px}
.club{top:1031px;left:536px;width:467px;height:303px;background:var(--teal)}
.club-name{top:1056px;left:740px;font-size:37px;font-weight:400;color:#fff}
.club-tag{top:1104px;left:740px;font-size:17px;line-height:21px;color:#21302d}
.checks{top:1088px;left:568px;list-style:none;color:#fff;font-size:14.7px}
.checks li{height:27.5px;display:flex;align-items:center;gap:9px}
.devices{top:1172px;left:731px;width:254px;height:113px;background:linear-gradient(180deg,#4a4f55,#23272b);border-radius:6px}
.join-badge{top:1365px;left:204px}
.join-text{top:1398px;left:353px;width:615px;font-size:17px;line-height:23px}
.packages-note{top:1477px;left:350px;font-size:18px}
.packages{top:1515px;left:313px;display:flex;gap:24px;font-size:17px;list-style:none}
.packages li{display:flex;align-items:center;gap:6px}
.packages li::before{content:"";width:9px;height:9px;background:var(--teal)}
.stat{top:1560px;left:241px;width:723px;height:95px;background:var(--teal);color:#fff;text-align:center}
.stat-line{margin-top:19px;font-size:19px}
.stat-figure{font-size:32px;margin-top:1px}
.tab{left:204px;width:270px;height:64px;border:1px solid var(--line);background:var(--tab);display:flex;align-items:center;justify-content:space-between;padding:0 16px;font-size:17px;color:var(--ink)}
.tab-active{background:#fff;border:2px solid var(--teal);color:var(--teal)}
.quote-head{top:1744px;left:537px;font-size:17px;display:flex;align-items:center;gap:8px}
.quote-bubble{top:1785px;left:537px;width:463px;height:83px;border:1px solid #cfcfcf;background:#fafafa;border-radius:3px;font-style:italic;font-size:15px;line-height:22px;padding:14px 18px}
.quote-avatar{top:1892px;left:542px;width:62px;height:62px;border-radius:50%;background:linear-gradient(180deg,#e9c98f,#d6a77c);border:3px solid #eee}
.divider{top:2013px;left:203px;width:800px;border-top:2px dotted #c9c9c9}
.connect{top:2039px;left:460px;width:280px;text-align:center;font-size:20px;color:var(--teal)}
.socials{top:2074px;left:523px;display:flex;gap:6px}
.socials span{width:34px;height:34px;border-radius:50%}
.copyright{top:2125px;left:460px;width:280px;text-align:center;font-size:17px}
.brand-foot{top:2074px;left:774px;font-size:24px;line-height:32px}
.brand-foot .brand-dot{width:11px;height:11px}
</style>
</head>
<body>
<p class="abs preheader">For anything about this mail you can contract us by <a href="#">click this link.</a></p>
<div class="abs mail"></div>

<div class="abs brand brand-top"><span class="brand-dot"></span>Kl4vo Amusements</div>
<div class="abs contact-btn contact-mail">
  <svg width="18" height="16" viewBox="0 0 18 16"><rect x="1" y="3" width="16" height="11" fill="none" stroke="#333" stroke-width="1.6"/><path d="M1 3l8 6 8-6" fill="none" stroke="#333" stroke-width="1.6"/></svg>
  Contact kl4vamu.com
</div>
<div class="abs contact-btn contact-phone">
  <svg width="18" height="18" viewBox="0 0 24 24"><path d="M6 2l4 5-2 3c1 3 3 5 6 6l3-2 5 4-3 4C10 21 3 14 2 5z" fill="none" stroke="#333" stroke-width="1.6"/></svg>
  1300 555 019
</div>

<div class="abs hero" role="img" aria-label="Photo of a city skyline at night with a lit bridge over the water"></div>

<h2 class="abs section-title" style="top:628px">WHO WE ARE:</h2>
<div class="abs section-rule" style="top:659px"></div>
<p class="abs about">KL4VO CLUB is a package experience that encases decades of proven and time-tested service in two interlinked but rarely combined industries: networking and gaming.<br>The company is driven by a team that's been experiencing and following the networking industry since the 1990s and the gaming industry since the 1980s. This has given ,..</p>
<a class="abs btn read-more">READ MORE&gt;</a>

<div class="abs offer"></div>
<div class="abs offer-title">Enjoy A priceless offer:
  <svg width="30" height="30" viewBox="0 0 30 30"><circle cx="15" cy="15" r="15" fill="var(--teal)"/><path d="M8 15h13M15 9l6 6-6 6" fill="none" stroke="#232a29" stroke-width="3"/></svg>
</div>
<p class="abs script offer-sub">we design a new altitude of fun and involvement every time</p>
<a class="abs btn offer-btn">FIND OUT TOP PERFORMER OF THE WEEKS</a>
<div class="abs agent" role="img" aria-label="Photo of a smiling support agent wearing a headset"></div>

<div class="abs invite">
  <p>We invite you to be a part of this epicenter of licensed betting and gaming, and pocket part of this monetary spoil! Once you join, you'll know what you've missed all along!</p>
  <p>Here are some unique advantages of becoming part of the growing KL4VO CLUB community accessible on all devices</p>
</div>

<div class="abs club"></div>
<h3 class="abs club-name">KL4VO CLUB</h3>
<p class="abs club-tag">THE SINGLE-STOP BETTING<br>AND GAMING PLATFORM</p>
<ul class="abs checks">
  <li><svg width="14" height="12" viewBox="0 0 14 12"><path d="M1 6l4 4 8-9" fill="none" stroke="#fff" stroke-width="2"/></svg>Professional</li>
  <li><svg width="14" height="12" viewBox="0 0 14 12"><path d="M1 6l4 4 8-9" fill="none" stroke="#fff" stroke-width="2"/></svg>Protected</li>
  <li><svg width="14" height="12" viewBox="0 0 14 12"><path d="M1 6l4 4 8-9" fill="none" stroke="#fff" stroke-width="2"/></svg>The Gaming</li>
  <li><svg width="14" height="12" viewBox="0 0 14 12"><path d="M1 6l4 4 8-9" fill="none" stroke="#fff" stroke-width="2"/></svg>SportsBook</li>
  <li><svg width="14" height="12" viewBox="0 0 14 12"><path d="M1 6l4 4 8-9" fill="none" stroke="#fff" stroke-width="2"/></svg>Referral Rewards</li>
  <li><svg width="14" height="12" viewBox="0 0 14 12"><path d="M1 6l4 4 8-9" fill="none" stroke="#fff" stroke-width="2"/></svg>Paid to Play</li>
  <li><svg width="14" height="12" viewBox="0 0 14 12"><path d="M1 6l4 4 8-9" fill="none" stroke="#fff" stroke-width="2"/></svg>Low Risk</li>
  <li><svg width="14" height="12" viewBox="0 0 14 12"><path d="M1 6l4 4 8-9" fill="none" stroke="#fff" stroke-width="2"/></svg>Full Support</li>
</ul>
<div class="abs devices" role="img" aria-label="Laptop, tablet and phone showing the gaming platform"></div>

<svg class="abs join-badge" width="118" height="118" viewBox="0 0 118 118">
  <polygon fill="var(--teal)" points="59,0 76,18 101,17 100,42 118,59 100,76 101,101 76,100 59,118 42,100 17,101 18,76 0,59 18,42 17,17 42,18"/>
  <text x="59" y="66" fill="#fff" font-family="Lato, sans-serif" font-weight="700" font-size="17" text-anchor="middle" transform="rotate(-40 59 59)">JOIN NOW</text>
</svg>
<p class="abs join-text">Join the KL4VO CLUB Membership and Rewards Program today to start earning income with a new dedicated Gaming and Sport Betting Service directed to the networking industry.</p>
<p class="abs script packages-note">we have these below packages...</p>
<ul class="abs packages">
  <li>BRONZE</li><li>SILVER</li><li>GOLD</li><li>RUBY</li><li>EMRALD</li><li>DIAMOND</li>
</ul>

<div class="abs stat">
  <p class="stat-line">By 2016 the size of the online global games market is forecasted to reach</p>
  <p class="stat-figure">$86.1 BILLION</p>
</div>

<h2 class="abs section-title" style="top:1690px">QUOTES:</h2>
<div class="abs section-rule" style="top:1719px"></div>

<a class="abs tab tab-active" style="top:1746px">This &nbsp;Week Best quotes
  <svg width="24" height="24" viewBox="0 0 24 24"><circle cx="12" cy="12" r="12" fill="var(--teal)"/><path d="M6 12h11M12 7l5 5-5 5" fill="none" stroke="#fff" stroke-width="2.4"/></svg></a>
<a class="abs tab" style="top:1822px">Last Month best quotes
  <svg width="24" height="24" viewBox="0 0 24 24"><circle cx="12" cy="12" r="12" fill="#8a8a8a"/><path d="M6 12h11M12 7l5 5-5 5" fill="none" stroke="#fff" stroke-width="2.4"/></svg></a>
<a class="abs tab" style="top:1899px">Last Year best quotes
  <svg width="24" height="24" viewBox="0 0 24 24"><circle cx="12" cy="12" r="12" fill="#8a8a8a"/><path d="M6 12h11M12 7l5 5-5 5" fill="none" stroke="#fff" stroke-width="2.4"/></svg></a>

<div class="abs quote-head">Todays Best Quotes
  <svg width="24" height="24" viewBox="0 0 24 24"><circle cx="12" cy="12" r="12" fill="var(--teal)"/><path d="M6 12h11M12 7l5 5-5 5" fill="none" stroke="#fff" stroke-width="2.4"/></svg>
</div>
<blockquote class="abs quote-bubble">Lorem ipsum dolor sit amet, consectetur adipisicing elit, sed do eiusmod tempor incididunt ut labore et</blockquote>
<div class="abs quote-avatar" role="img" aria-label="Portrait photo of the quoted member"></div>

<div class="abs divider"></div>
<p class="abs script connect">Get connected by us</p>
<div class="abs socials">
  <span style="background:#3b5998"></span><span style="background:#1da1f2"></span><span style="background:#0a78b5"></span><span style="background:#dd4b39"></span>
</div>
<p class="abs copyright">© 2016 KL4VOENT</p>
<div class="abs brand brand-foot"><span class="brand-dot"></span>Kl4vo Amusements</div>
</body>
</html>
```